Design of Stationery (Business Card, Letterhead and Envelope) for Investment Company
Kestrelmoor Capital Associates Limited
Design of Stationery (Business Card, Letterhead and Envelope) for Investment Company - Financial Services
Creative Brief
Simple
Tunde A. Ibekwe
Director
7C, Dunmore Crescent, Osapa Garden Estate, Lekki Peninsula, Lagos
tunde@kestrelmoorng.example
www.kestrelmoorng.example
RC 458290
The back of the business card should have the logo of the company on navy blue background - please see the logo uploaded. Below the logo should be the words: "INVESTMENTS. ADVICE. VALUE CREATION".

```html
<!DOCTYPE html>
<html lang="en">
<head>
<meta charset="UTF-8">
<title>Kestrelmoor Capital Associates – Business Card</title>
<link rel="stylesheet" href="https://fonts.googleapis.com/css2?family=Montserrat:wght@400;500;600&display=swap">
<style>
  :root {
    --page-bg: #e6e7ea;
    --card-white: #ffffff;
    --navy: #2f4369;
    --navy-deep: #26385a;
    --accent-grey: #9a9ca1;
    --text-white: #ffffff;
    --text-soft: #dfe4ee;
  }
  * { margin: 0; padding: 0; box-sizing: border-box; }
  html, body {
    width: 1200px;
    height: 901px;
    overflow: hidden;
    background: var(--page-bg);
    font-family: "Montserrat", sans-serif;
  }
  .business-card {
    position: absolute;
    left: 150px;
    top: 193px;
    width: 900px;
    height: 514px;
    border-radius: 34px;
    overflow: hidden;
    background: var(--card-white);
    box-shadow: 0 10px 30px rgba(0,0,0,0.18);
  }
  .card-shapes { position: absolute; inset: 0; }
  .brand {
    position: absolute;
    left: 70px;
    top: 150px;
    width: 380px;
    text-align: center;
    color: var(--navy);
    font-weight: 600;
  }
  .brand-square {
    display: block;
    width: 92px;
    height: 92px;
    margin: 0 auto 26px;
    background: var(--navy);
    border-radius: 6px;
  }
  .brand-name {
    font-size: 40px;
    letter-spacing: 1px;
    line-height: 1;
  }
  .brand-sub {
    margin-top: 10px;
    font-size: 15px;
    letter-spacing: 5.2px;
    line-height: 1;
  }
  .contact {
    position: absolute;
    right: 46px;
    top: 0;
    bottom: 0;
    width: 360px;
    color: var(--text-white);
    text-align: right;
  }
  .person-name {
    position: absolute; right: 0; top: 74px;
    font-size: 22px; font-weight: 500; letter-spacing: 1.5px;
    text-transform: uppercase;
  }
  .person-title {
    position: absolute; right: 0; top: 106px;
    font-size: 15px; color: var(--text-soft);
  }
  .address {
    position: absolute; right: 0; top: 186px;
    font-size: 15px; line-height: 1.5;
  }
  .lines {
    position: absolute; right: 0; top: 300px;
    list-style: none;
    font-size: 14px;
  }
  .lines li {
    display: flex; justify-content: flex-end; align-items: center;
    gap: 12px; height: 31px;
  }
  .lines svg { width: 16px; height: 16px; flex: none; }
</style>
</head>
<body>
  <div class="business-card">
    <svg class="card-shapes" viewBox="0 0 900 514" aria-hidden="true">
      <path d="M 560 0 C 470 130, 600 330, 420 514 L 395 514 C 575 330, 440 130, 530 0 Z" fill="var(--accent-grey)"/>
      <path d="M 575 0 C 485 130, 615 330, 435 514 L 900 514 L 900 0 Z" fill="var(--navy)"/>
    </svg>

    <div class="brand">
      <span class="brand-square"></span>
      <div class="brand-name">KESTRELMOOR</div>
      <div class="brand-sub">CAPITAL ASSOCIATES</div>
    </div>

    <div class="contact">
      <p class="person-name">Tunde A. Ibekwe</p>
      <p class="person-title">Managing Director</p>
      <p class="address">7C Dunmore Crescent,<br>Osapa LKP</p>
      <ul class="lines">
        <li>012 555 0147
          <svg viewBox="0 0 16 16"><path d="M4 1.5l2.2 3-1.4 1.4c.8 1.8 2.2 3.2 4 4l1.4-1.4 3 2.2-1.2 2.6C6.6 13 3 9.4 1.7 2.7z" fill="#fff"/></svg>
        </li>
        <li>012 555 0148
          <svg viewBox="0 0 16 16"><rect x="4.5" y="1" width="7" height="14" rx="1.3" fill="none" stroke="#fff" stroke-width="1.4"/><circle cx="8" cy="12.6" r=".9" fill="#fff"/></svg>
        </li>
        <li>012 555 0149
          <svg viewBox="0 0 16 16"><rect x="1.5" y="5" width="13" height="8" rx="1" fill="#fff"/><rect x="4" y="2" width="8" height="4" fill="none" stroke="#fff" stroke-width="1.3"/></svg>
        </li>
        <li>tunde@kestrelmoorng.example
          <svg viewBox="0 0 16 16"><rect x="1.5" y="3.5" width="13" height="9" rx="1" fill="#fff"/><path d="M1.8 4l6.2 5 6.2-5" fill="none" stroke="var(--navy)" stroke-width="1.2"/></svg>
        </li>
        <li>www.kestrelmoorng.example
          <svg viewBox="0 0 16 16"><circle cx="8" cy="8" r="6.3" fill="none" stroke="#fff" stroke-width="1.3"/><ellipse cx="8" cy="8" rx="2.6" ry="6.3" fill="none" stroke="#fff" stroke-width="1.1"/><path d="M2 8h12" stroke="#fff" stroke-width="1.1"/></svg>
        </li>
      </ul>
    </div>
  </div>
</body>
</html>
```